Business card design needed

Marketing Communications

Target Market(s)

prospective clients in the marketing communications industry

Industry/Entity Type

Business

Contact Information for Business Card

merel vasko
Marketing Communications
tolupar@quennet.com
0462 815947

Logo Text

merel vasko

Logo styles of interest
Abstract Logo
Requirements
Must have
• An appropriate abstract logo. only a one or two colour design
Nice to have
• Logo to portray the growth of a marketing brief
Should not have
• no more than two colours maximum

```html
<!DOCTYPE html>
<html lang="en">
<head>
<meta charset="utf-8">
<title>Merel Vasko – Business Card</title>
<link rel="stylesheet" href="https://fonts.googleapis.com/css2?family=Fredoka:wght@500;600&display=swap">
<style>
  :root {
    --brand-blue: #2a9bcb;
    --card-tint: #e8f4f9;
    --card-light: #f4fafd;
    --page-bg: #ffffff;
  }
  * { margin: 0; padding: 0; box-sizing: border-box; }
  html, body {
    width: 1200px;
    height: 741px;
    overflow: hidden;
    background: var(--page-bg);
  }
  .card {
    position: absolute;
    left: 46px;
    top: 49px;
    width: 1107px;
    height: 643px;
    font-family: "Fredoka", sans-serif;
    color: var(--brand-blue);
    text-transform: uppercase;
  }
  .card__backdrop {
    position: absolute;
    inset: 0;
    background: linear-gradient(135deg, var(--card-tint) 0%, var(--card-light) 50%, var(--card-tint) 100%);
  }
  .card__top-band {
    position: absolute;
    left: 0; top: 0;
    width: 100%;
    height: 70px;
    background: var(--brand-blue);
  }
  .card__rule {
    position: absolute;
    left: 0; top: 492px;
    width: 100%;
    height: 15px;
    background: var(--brand-blue);
  }
  .media-icon {
    position: absolute;
    background: var(--brand-blue);
    border-radius: 8px;
  }
  .media-icon--tv { left: 21px; top: 170px; width: 101px; height: 154px; border-radius: 22px; }
  .media-icon--print { left: 173px; top: 191px; width: 98px; height: 135px; }
  .media-icon--screen { left: 324px; top: 189px; width: 111px; height: 138px; }
  .tagline {
    position: absolute;
    left: 15px;
    top: 355px;
    font-size: 41px;
    font-weight: 600;
    line-height: 46px;
    letter-spacing: 1px;
  }
  .contact {
    position: absolute;
    right: 7px;
    top: 205px;
    text-align: right;
    font-weight: 600;
  }
  .contact__name {
    font-size: 90px;
    line-height: 86px;
    letter-spacing: 4px;
  }
  .contact__email,
  .contact__phone {
    font-size: 38px;
    line-height: 37px;
    letter-spacing: 1px;
  }
  .contact__email { margin-top: 6px; }
</style>
</head>
<body>
  <div class="card">
    <div class="card__backdrop" role="img" aria-label="Light blue diagonal stripe background pattern"></div>
    <div class="card__top-band"></div>

    <div class="media-icon media-icon--tv" role="img" aria-label="Television icon"></div>
    <div class="media-icon media-icon--print" role="img" aria-label="Newspaper icon"></div>
    <div class="media-icon media-icon--screen" role="img" aria-label="Desktop computer icon"></div>

    <p class="tagline">Marketing<br>Communications</p>

    <div class="contact">
      <p class="contact__name">Merel Vasko</p>
      <p class="contact__email">tolupar@quennet.com</p>
      <p class="contact__phone">0462 815947</p>
    </div>

    <div class="card__rule"></div>
  </div>
</body>
</html>
```